Sehr angenehme und professionelle Zusammenarbeit!
Zielgruppe
Ich bin ein Consultant, der sich jetzt selbständig macht. Alles weitere steht in meinen Briefing. Dort findet ihr Fotos, mein Logo und damit auch die Farben, die ich mir wünsche. Meine Zielgruppe sind überwiegend Firmen, aber auch deren Mitarbeitende.
Aufgabenstellung
Die Struktur habe ich versucht zu beschreiben und hoffentlich auch alles über mich und mein Business. Ich freue mich auf eure kreativen und individuellen Vorschläge und bemühe mich zeitnah Feedback zu geben. Manchmal kann es den einen oder anderen Tag dauern. Bei Fragen gerne melden. Ich werde die Fragen, die für alle relevant sind auch im allgemeinen Kommentarfeld veröffentlichen.

```html
<!DOCTYPE html>
<html lang="de">
<head>
<meta charset="utf-8">
<title>Robert Thalberg – Beratung für komplexe Personalsituationen</title>
<link href="https://fonts.googleapis.com/css2?family=EB+Garamond:wght@400;600;700&family=Lato:wght@400;700&family=Nunito+Sans:wght@400;600&display=swap" rel="stylesheet">
<style>
  :root {
    --navy: #0f3d8c;
    --ink: #16181d;
    --muted: #6b6f78;
    --soft-bg: #f7f9fb;
    --white: #ffffff;
    --shade: #eceef2;
  }
  * { box-sizing: border-box; margin: 0; padding: 0; }
  html, body { width: 1200px; height: 2640px; overflow: hidden; }
  body { position: relative; background: var(--white); color: var(--ink); font-family: "Lato", sans-serif; }
  .serif { font-family: "EB Garamond", serif; }
  .ui { font-family: "Nunito Sans", sans-serif; }
  .abs { position: absolute; }

  /* header */
  .site-header { position: absolute; top: 0; left: 0; width: 1200px; height: 67px; background: var(--soft-bg); border-bottom: 1px solid #eef0f3; }
  .brand { position: absolute; left: 94px; top: 22px; display: flex; align-items: center; gap: 10px; font-family: "EB Garamond", serif; font-size: 21px; color: var(--ink); }
  .brand-dot { width: 16px; height: 16px; border-radius: 50%; background: var(--navy); }
  .main-nav { position: absolute; top: 15px; right: 93px; display: flex; align-items: center; font-family: "Nunito Sans", sans-serif; font-size: 14px; }
  .main-nav a { color: var(--muted); text-decoration: none; margin-right: 27px; }
  .main-nav a.active { color: var(--ink); }
  .btn { display: inline-block; background: var(--navy); color: var(--white); font-family: "Nunito Sans", sans-serif; font-weight: 600; font-size: 13px; text-decoration: none; padding: 0 15px; height: 36px; line-height: 36px; }
  .main-nav .btn { color: var(--white); margin: 0; padding: 0 15px; width: 82px; text-align: center; }

  /* hero */
  .hero { position: absolute; top: 67px; left: 0; width: 1200px; height: 740px; background: var(--soft-bg); }
  .hero-photo { position: absolute; left: 561px; top: 0; width: 639px; height: 513px; background: linear-gradient(90deg, #e6e7ea 0%, #9a9ca3 35%, #c9cbd0 55%, #e54a8e 75%, #f29a4a 100%); }
  .hero-title { position: absolute; left: 94px; top: 160px; width: 440px; font-family: "EB Garamond", serif; font-weight: 400; font-size: 53px; line-height: 60px; }
  .hero-title b { font-weight: 700; }
  .scroll-arrow { position: absolute; left: 92px; top: 461px; }
  .intro { position: absolute; top: 569px; font-size: 13.2px; line-height: 20px; width: 494px; }
  .intro.left { left: 94px; }
  .intro.right { left: 613px; }

  /* win section */
  .win-photo { position: absolute; left: 0; top: 889px; width: 578px; height: 433px; background: linear-gradient(160deg, #f2f3f5 0%, #d9dce1 45%, #2d3f73 70%, #e7e9ec 100%); }
  .slider-dots { position: absolute; left: 25px; top: 1149px; }
  .slider-dots span { display: block; width: 8px; height: 8px; border-radius: 50%; background: var(--white); margin-bottom: 16px; }
  .win-title { position: absolute; left: 613px; top: 958px; font-family: "EB Garamond", serif; font-weight: 400; font-size: 52px; line-height: 60px; }
  .win-title b { font-weight: 700; }
  .win-text { position: absolute; left: 613px; top: 1107px; width: 524px; font-size: 13.2px; line-height: 20px; }
  .win-btn { position: absolute; left: 613px; top: 1254px; }

  /* offers */
  .offers { position: absolute; top: 1402px; left: 0; width: 1200px; height: 605px; background: var(--soft-bg); overflow: hidden; }
  .offers-title { position: absolute; left: 94px; top: 54px; font-family: "EB Garamond", serif; font-weight: 400; font-size: 52px; line-height: 60px; }
  .offers-title b { font-weight: 700; }
  .offer-card { position: absolute; top: 162px; width: 283px; height: 385px; background: var(--white); }
  .offer-card .card-photo { width: 100%; height: 100%; }
  .offer-card.featured .card-photo { height: 186px; }
  .card-body { padding: 22px 20px; }
  .card-title { font-family: "EB Garamond", serif; font-weight: 700; font-size: 26px; line-height: 35px; }
  .card-sub { font-family: "Nunito Sans", sans-serif; font-size: 13px; color: var(--muted); margin-top: 10px; }
  .card-body .btn { margin-top: 24px; width: 79px; text-align: center; padding: 0; }

  /* about */
  .about-shade { position: absolute; left: 180px; top: 2120px; width: 180px; height: 397px; background: var(--shade); }
  .about-photo { position: absolute; left: 195px; top: 2098px; width: 324px; height: 405px; background: linear-gradient(180deg, #e9e9e8 0%, #d6c3b2 40%, #c9d8ee 70%, #23375f 100%); }
  .about-title { position: absolute; left: 586px; top: 2118px; font-family: "EB Garamond", serif; font-weight: 400; font-size: 48px; line-height: 60px; }
  .about-title b { font-weight: 700; }
  .about-text { position: absolute; left: 586px; top: 2322px; width: 520px; font-size: 13.2px; line-height: 20px; }
  .about-text strong { font-weight: 700; }
  .about-btn { position: absolute; left: 586px; top: 2429px; }

  /* footer */
  .copyright { position: absolute; left: 173px; top: 2600px; font-size: 12px; color: var(--muted); }
  .social { position: absolute; top: 2600px; left: 932px; display: flex; gap: 17px; }
  .social span { width: 20px; height: 20px; border-radius: 50%; background: var(--ink); }
</style>
</head>
<body>
  <header class="site-header">
    <div class="brand"><span class="brand-dot"></span>Robert Thalberg</div>
    <nav class="main-nav">
      <a class="active" href="#">Home</a>
      <a href="#">Angebote</a>
      <a href="#">Über mich</a>
      <a class="btn" href="#">Kontakt</a>
    </nav>
  </header>

  <section class="hero">
    <div class="hero-photo" role="img" aria-label="Foto: Berater im Gespräch mit einer Kollegin, rechts farbig verwischte Person"></div>
    <h1 class="hero-title"><b>Für alle. Das Beste.</b> Beratung für komplexe Personal&shy;situationen.</h1>
    <svg class="scroll-arrow abs" width="10" height="54" viewBox="0 0 10 54" aria-hidden="true">
      <line x1="5" y1="0" x2="5" y2="52" stroke="#16181d" stroke-width="1"/>
      <polyline points="1,47 5,52 9,47" fill="none" stroke="#16181d" stroke-width="1"/>
    </svg>
    <p class="intro left">Personalprobleme sind eine normale Begleiterscheinung in unserer Zeit voll Wandel. Im Daily Business werden diese Situationen jedoch selten tiefer analysiert und häufig nur kosmetisch behandelt. Ein Aussitzen hier, eine Mediation dort, ein plötzliches Abfindungsangebot da. Vielleicht auch schon zahlreiche Gespräche oder Coachings, die nicht zur gewünschten Veränderung führten.<br>Die Folge: die Motivation sinkt. Nicht nur bei dem/der jeweiligen Mitabeitenden,</p>
    <p class="intro right">auch im Teamumfeld und bei der Führungskraft. Frustration steigt, es kommt zu Fehlzeiten, die Produktivität lässt nach, mitunter können Ziele nicht erreicht werden. Die Gerüchteküche köchelt vor sich hin.<br>Meine Beratung und Prozessbegleitung schließt hier eine Lücke. Sie bietet nachhaltige Lösungen bei komplexen und dysfunktionalen Personalsituationen an, die alle Seiten einbeziehen: Mitarbeitende/r. Führungskraft. Organisation.</p>
  </section>

  <section class="win">
    <div class="win-photo" role="img" aria-label="Foto: Mann im Anzug mit erhobenen Armen unter einer weißen Brückenkonstruktion"></div>
    <div class="slider-dots"><span></span><span></span><span></span></div>
    <h2 class="win-title">Von Lose zu <b>Win</b><br><b>für alle Seiten.</b></h2>
    <p class="win-text">Während auf individueller Ebene Menschen ihr Potenzial nicht entfalten können und oft lange an der Situation leiden, entstehen auf organisationaler Ebene wirtschaftliche Einbußen und Imageschäden. Selten ist nur eine Person betroffen, auch wenn es sich oft auf eine Person fokussiert. Die Ursachen sind multifaktoriell und langwierig, die negative Wirkung strahlt auf den/die Mitarbeitende/n, die Führungskraft, das Team und die Abteilung aus.</p>
    <a class="btn win-btn" href="#">Zum Kennenlerngespräch</a>
  </section>

  <section class="offers">
    <h2 class="offers-title">Meine <b>Angebote</b></h2>
    <article class="offer-card featured" style="left:94px;">
      <div class="card-photo" role="img" aria-label="Foto: zwei Männer im Gespräch am Flussufer" style="background:linear-gradient(180deg,#5d7a4a 0%,#8fa07a 50%,#9fb2cf 100%);"></div>
      <div class="card-body">
        <h3 class="card-title">Prozessberatung und – begleitung</h3>
        <p class="card-sub">Ganzheitlich vom Problem zur Lösung</p>
        <a class="btn" href="#">Mehr</a>
      </div>
    </article>
    <article class="offer-card" style="left:404px;">
      <div class="card-photo" role="img" aria-label="Foto: Berater im hellblauen Hemd im Gespräch im Grünen" style="background:linear-gradient(180deg,#8f9a7c 0%,#b9c2b0 40%,#7fa3d6 80%,#2c3d63 100%);"></div>
    </article>
    <article class="offer-card" style="left:713px;">
      <div class="card-photo" role="img" aria-label="Foto: zwei Personen gehen auf einem Feldweg" style="background:linear-gradient(180deg,#3b4252 0%,#a9a59c 45%,#cfcbc2 100%);"></div>
    </article>
    <article class="offer-card" style="left:1024px;">
      <div class="card-photo" role="img" aria-label="Foto: zwei Männer vor einer Stadtsilhouette" style="background:linear-gradient(90deg,#c7cdd4 0%,#e7ebf0 50%,#b4c8e6 100%);"></div>
    </article>
  </section>

  <section class="about">
    <div class="about-shade"></div>
    <div class="about-photo" role="img" aria-label="Porträtfoto des Beraters im blauen Sakko"></div>
    <h2 class="about-title">Ich bin <b>Robert Thalberg</b><br>und mein Anspruch ist:<br><b>Für alle. Das Beste.</b></h2>
    <p class="about-text"><strong>Meine Motivation:</strong><br>Ich möchte Menschen unterstützen, sich aus dysfunktionalen Arbeitssituationen zu lösen, ihr Potenzial zu erkennen und auszuleben. Dafür setze ich mich als selbstständiger Berater ein, nach 25 Jahren im Personalbereich, zumeist in Führungspositionen.</p>
    <a class="btn about-btn" href="#">Mehr über mich</a>
  </section>

  <footer>
    <p class="copyright">© 2022 - RTConsulting</p>
    <div class="social" aria-label="Soziale Netzwerke"><span></span><span></span><span></span></div>
  </footer>
</body>
</html>
```